Harbor Business Cards

I need a business card designed with the following information.

Company Name: Harbor Wealth Management
Name: BriAnne Dockery
Title: Executive Assistant
Cell: (555) 555-0173
Direct Line: (555) 555-0148
Email: brianne@harborwmx.com
Address: 20537 W. Marlowe PKWY Ste. B
Cedarvale, ST 77390

I have attached the logo.
I would like it in navy blue and silver.
Thanks.

```html
<!DOCTYPE html>
<html lang="en">
<head>
<meta charset="utf-8">
<title>Harbor Wealth Management – Business Card</title>
<link href="https://fonts.googleapis.com/css2?family=Marcellus&family=Lato:wght@400&display=swap" rel="stylesheet">
<style>
  :root {
    --backdrop: #2f2a27;
    --card-white: #eef0f2;
    --navy: #16284c;
    --navy-deep: #12213f;
    --silver: #c9ced6;
    --silver-soft: #aeb5c0;
  }
  html, body {
    margin: 0;
    padding: 0;
    width: 1200px;
    height: 769px;
    overflow: hidden;
    background: var(--backdrop);
  }
  .canvas {
    position: relative;
    width: 1200px;
    height: 769px;
  }
  .card {
    position: absolute;
    top: 236px;
    width: 520px;
    height: 297px;
    box-sizing: border-box;
    border-radius: 3px;
    box-shadow: 0 10px 24px rgba(0,0,0,0.35);
  }
  .card-front {
    left: 60px;
    background: var(--card-white);
    display: flex;
    flex-direction: column;
    align-items: center;
    justify-content: center;
  }
  .brand-mark {
    width: 40px;
    height: 40px;
    background: var(--navy);
    margin-bottom: 22px;
  }
  .brand-name {
    font-family: "Marcellus", serif;
    color: var(--navy);
    text-align: center;
    text-transform: uppercase;
    margin: 0;
    font-weight: 400;
    line-height: 1.2;
  }
  .brand-name .primary {
    display: block;
    font-size: 40px;
    letter-spacing: 14px;
    padding-left: 14px;
  }
  .brand-name .secondary {
    display: block;
    font-size: 13px;
    letter-spacing: 5px;
    padding-left: 5px;
    margin-top: 4px;
  }
  .card-back {
    left: 620px;
    background: linear-gradient(160deg, var(--navy) 0%, var(--navy-deep) 100%);
    padding: 26px 28px;
    font-family: "Lato", sans-serif;
    color: var(--silver);
    text-align: right;
  }
  .person-name {
    font-size: 19px;
    letter-spacing: 1px;
    text-transform: uppercase;
    margin: 0;
    font-weight: 400;
    font-family: "Marcellus", serif;
    color: var(--silver);
  }
  .person-title {
    font-size: 12px;
    margin: 2px 0 14px;
    color: var(--silver-soft);
  }
  .address {
    font-size: 11.5px;
    line-height: 1.45;
    margin: 0 0 10px;
    font-style: normal;
    color: var(--silver-soft);
  }
  .contact-list {
    list-style: none;
    margin: 0;
    padding: 0;
    font-size: 11.5px;
    line-height: 1.75;
  }
  .contact-list li {
    display: flex;
    justify-content: flex-end;
    align-items: center;
    gap: 8px;
  }
  .contact-list svg {
    width: 11px;
    height: 11px;
    fill: none;
    stroke: var(--silver);
    stroke-width: 1.3;
  }
</style>
</head>
<body>
<main class="canvas">
  <section class="card card-front" aria-label="Card front">
    <div class="brand-mark"></div>
    <h1 class="brand-name">
      <span class="primary">Harbor</span>
      <span class="secondary">Wealth Management</span>
    </h1>
  </section>

  <section class="card card-back" aria-label="Card back">
    <h2 class="person-name">BriAnne Dockery</h2>
    <p class="person-title">Executive Assistant</p>
    <address class="address">
      20537 W. Marlowe PKWY Ste. B<br>
      Cedarvale, ST 77390
    </address>
    <ul class="contact-list">
      <li>(555) 555-0148
        <svg viewBox="0 0 12 12" aria-hidden="true"><path d="M2.5 1.5 L4.5 1.5 L5.3 3.8 L4 4.8 Q5 7 7.2 8 L8.2 6.7 L10.5 7.5 L10.5 9.5 Q10.5 10.5 9.5 10.5 Q2 10 1.5 2.5 Q1.5 1.5 2.5 1.5 Z"/></svg>
      </li>
      <li>(555) 555-0173
        <svg viewBox="0 0 12 12" aria-hidden="true"><rect x="3" y="1" width="6" height="10" rx="1"/><line x1="5.3" y1="9.3" x2="6.7" y2="9.3"/></svg>
      </li>
      <li>brianne@harborwmx.com
        <svg viewBox="0 0 12 12" aria-hidden="true"><rect x="1" y="2.5" width="10" height="7"/><polyline points="1,2.5 6,6.5 11,2.5"/></svg>
      </li>
      <li>www.harborwmx.com
        <svg viewBox="0 0 12 12" aria-hidden="true"><circle cx="6" cy="6" r="4.8"/><ellipse cx="6" cy="6" rx="2" ry="4.8"/><line x1="1.2" y1="6" x2="10.8" y2="6"/></svg>
      </li>
    </ul>
  </section>
</main>
</body>
</html>
```